Belarde's Plumbing, Heating, and AC Buisness card

I need a business card design for my Plumbing Heating and AC company. We are based out of North Windham, CT, and offer residential and light commercial services. I am looking for something that incorporates a water droplet, snowflake, and flame. I would like it to be Modern and different from a typical business card but needs to communicate confidence and security.

```html
<!DOCTYPE html>
<html lang="en">
<head>
<meta charset="utf-8">
<title>Belarde's Plumbing, Heating, and AC — Business Card</title>
<link href="https://fonts.googleapis.com/css2?family=Montserrat:wght@700;800&family=Nunito:wght@600;700&display=swap" rel="stylesheet">
<style>
  :root {
    --backdrop: #2a2a2c;
    --card-dark: #0b0b0c;
    --card-dark-mark: #1a1a1c;
    --card-light: #ffffff;
    --brand-blue: #1f4fb8;
    --sky-blue: #1f8ee0;
    --accent-orange: #f07a1c;
    --text-blue: #23349a;
  }
  * { box-sizing: border-box; margin: 0; padding: 0; }
  html, body {
    width: 1200px; height: 900px; overflow: hidden;
    background: var(--backdrop);
  }
  .canvas { position: relative; width: 1200px; height: 900px; }

  .card {
    position: absolute;
    width: 700px; height: 400px;
    border-radius: 26px;
    overflow: hidden;
    box-shadow: 0 18px 40px rgba(0,0,0,.45);
  }

  /* Front */
  .card--front { left: 60px; top: 40px; background: var(--card-dark); }
  .card--front .faint-mark {
    position: absolute; right: -60px; top: -40px;
    width: 360px; height: 360px; border-radius: 50%;
    background: var(--card-dark-mark);
  }
  .card--front .brand {
    position: absolute; left: 140px; top: 150px;
    display: flex; align-items: center; gap: 22px;
  }
  .brand-dot {
    width: 84px; height: 84px; border-radius: 50%;
    background: var(--sky-blue); flex: none;
  }
  .brand-name {
    font-family: "Montserrat", sans-serif; font-weight: 800;
    color: var(--sky-blue); line-height: 1.05;
  }
  .brand-name .line-main { display: block; font-size: 54px; letter-spacing: 2px; }
  .brand-name .line-sub { display: block; font-size: 17px; letter-spacing: 1px; }

  /* Back */
  .card--back { left: 440px; top: 470px; background: var(--card-light); }
  .card--back .brand-name { color: var(--brand-blue); position: absolute; left: 40px; top: 38px; }
  .card--back .brand-name .line-main { font-size: 60px; }
  .card--back .brand-name .line-sub { font-size: 18px; }
  .card--back .mark-disc {
    position: absolute; right: 50px; top: 70px;
    width: 250px; height: 250px; border-radius: 50%;
    background: var(--sky-blue);
  }
  .person { position: absolute; left: 44px; top: 168px; font-family: "Montserrat", sans-serif; }
  .person-name { color: var(--text-blue); font-weight: 800; font-size: 22px; letter-spacing: 1px; }
  .person-role { color: var(--accent-orange); font-weight: 800; font-size: 16px; letter-spacing: 1px; margin-top: 2px; }
  .address {
    position: absolute; left: 44px; top: 234px;
    font-family: "Nunito", sans-serif; font-weight: 600;
    color: var(--text-blue); font-size: 17px; line-height: 1.3;
  }
  .contacts {
    position: absolute; left: 44px; top: 308px; list-style: none;
    font-family: "Nunito", sans-serif; font-weight: 600;
    color: var(--text-blue); font-size: 17px; line-height: 1.5;
  }
  .contacts li { display: flex; align-items: center; gap: 10px; }
  .contacts svg { width: 16px; height: 16px; flex: none; }
</style>
</head>
<body>
<div class="canvas">

  <section class="card card--front" aria-label="Business card front">
    <div class="faint-mark"></div>
    <div class="brand">
      <div class="brand-dot"></div>
      <div class="brand-name">
        <span class="line-main">BELARDE'S</span>
        <span class="line-sub">PLUMBING, HEATING AND AC</span>
      </div>
    </div>
  </section>

  <section class="card card--back" aria-label="Business card back">
    <div class="brand-name">
      <span class="line-main">BELARDE'S</span>
      <span class="line-sub">PLUMBING, HEATING AND AC</span>
    </div>
    <div class="mark-disc"></div>

    <div class="person">
      <p class="person-name">DANIEL HARLOW</p>
      <p class="person-role">MANAGING DIRECTOR</p>
    </div>

    <p class="address">118 Linden Street<br>Unit 2, North Windham<br>CT 06256</p>

    <ul class="contacts">
      <li>
        <svg viewBox="0 0 16 16" aria-hidden="true"><path d="M3.5 1.5l2.5 2.5-1.5 2a8 8 0 0 0 5.5 5.5l2-1.5 2.5 2.5-2 2C7 14.5 1.5 9 1.5 3.5z" fill="none" stroke="var(--accent-orange)" stroke-width="1.6" stroke-linejoin="round"/></svg>
        860-555-0147
      </li>
      <li>
        <svg viewBox="0 0 16 16" aria-hidden="true"><rect x="1" y="3" width="14" height="10" rx="1" fill="var(--accent-orange)"/><path d="M1.5 3.5L8 9l6.5-5.5" fill="none" stroke="#fff" stroke-width="1.3"/></svg>
        daniel@belardes.com
      </li>
      <li>
        <svg viewBox="0 0 16 16" aria-hidden="true"><g fill="none" stroke="var(--accent-orange)" stroke-width="1.3"><circle cx="8" cy="8" r="6.5"/><ellipse cx="8" cy="8" rx="3" ry="6.5"/><path d="M1.5 8h13M2.5 4.8h11M2.5 11.2h11"/></g></svg>
        www.belardes.com
      </li>
    </ul>
  </section>

</div>
</body>
</html>
```